Brook Vantage claims recovery services

Its a new company in Dubai UAE. The company activity is debt management, debt collection, loans settlements and restructuring. The company involved in any business or sector requires debt management including government entities, Medical & Health care sector, Banks & finance companies, SME's and commercial business.

Target Market(s)

government entities, Medical & Health care sector, Banks & finance companies, SME's and commercial business.

Industry/Entity Type

Financial Service

Number of Pages Required

5+ page

Requirements
Must have
• Focus on the services not the team and clients
Should not have
• Colorful . Shouldn't have Client testimonial and our clients

```html
<!DOCTYPE html>
<html lang="en">
<head>
<meta charset="utf-8">
<title>Brook Vantage — Claims Recovery Services</title>
<link href="https://fonts.googleapis.com/css2?family=Cinzel:wght@400;700&family=Lato:wght@700;900&family=Open+Sans:wght@400;600;700&family=Roboto+Condensed:wght@400;700&display=swap" rel="stylesheet">
<style>
  :root {
    --navy: #234f75;
    --navy-deep: #1d4466;
    --blue: #2c6a9c;
    --grey-head: #8d8d8d;
    --text: #555555;
    --band: #efefef;
    --white: #ffffff;
    --footer: #333333;
    --footer-line: #555555;
    --nav: #8a8a8a;
  }
  * { box-sizing: border-box; margin: 0; padding: 0; }
  html, body { width: 1200px; height: 2187px; overflow: hidden; background: var(--white); }
  body { position: relative; font-family: "Open Sans", sans-serif; color: var(--text); }
  h1, h2, h3, h4 { font-weight: 400; }
  section, header, footer { position: absolute; left: 0; width: 1200px; }

  /* Header */
  .site-header { top: 0; height: 128px; background: var(--white); }
  .brand { position: absolute; left: 80px; top: 34px; display: flex; align-items: center; gap: 16px; }
  .brand-square { width: 52px; height: 52px; background: var(--navy); }
  .brand-text { display: flex; flex-direction: column; }
  .brand-name { font-family: "Cinzel", serif; font-size: 32px; color: var(--navy); line-height: 1; white-space: nowrap; }
  .brand-tag { font-family: "Cinzel", serif; font-size: 10px; letter-spacing: 5px; color: var(--navy); margin-top: 6px; white-space: nowrap; }
  .main-nav { position: absolute; top: 49px; left: 487px; display: flex; gap: 40px; font-family: "Cinzel", serif; font-size: 19px; color: var(--nav); }
  .main-nav .active { color: var(--navy); }

  /* Hero */
  .hero { top: 128px; height: 544px; background: linear-gradient(100deg, #f4f5f6 0%, #e6e8ea 35%, #b9bdc2 62%, #6f747a 85%, #4b4f54 100%); }
  .hero-headline { position: absolute; left: 80px; top: 96px; font-family: "Lato", sans-serif; font-weight: 900; font-size: 42px; line-height: 63px; color: var(--navy); text-transform: uppercase; }
  .btn-outline { position: absolute; border: 1.5px solid var(--navy); color: var(--navy); display: flex; align-items: center; justify-content: center; }
  .hero .btn-outline { left: 77px; top: 314px; width: 198px; height: 62px; font-family: "Cinzel", serif; font-size: 22px; }

  /* Sectors */
  .sectors { top: 672px; height: 312px; background: var(--band); }
  .sector { position: absolute; top: 57px; width: 260px; text-align: center; }
  .sector-icon { width: 114px; height: 114px; border-radius: 50%; background: var(--white); margin: 0 auto; display: flex; align-items: center; justify-content: center; }
  .sector-label { margin-top: 28px; font-family: "Cinzel", serif; font-size: 20px; line-height: 31px; color: #333; }

  /* Welcome */
  .welcome { top: 984px; height: 384px; background: var(--white); }
  .section-title { font-family: "Cinzel", serif; font-size: 47px; color: var(--grey-head); white-space: nowrap; }
  .section-title strong { font-weight: 400; color: var(--navy); }
  .welcome .section-title { position: absolute; left: 80px; top: 58px; font-size: 37px; }
  .welcome-copy { position: absolute; left: 80px; top: 126px; width: 616px; font-size: 15.5px; line-height: 25px; }
  .welcome .btn-outline { left: 77px; top: 267px; width: 146px; height: 52px; font-family: "Roboto Condensed", sans-serif; font-size: 21px; }
  .welcome-mark { position: absolute; left: 786px; top: 83px; width: 338px; height: 223px; background: radial-gradient(circle at 50% 40%, #fbfbfb, #d6d6d6); display: flex; align-items: center; justify-content: center; font-family: "Cinzel", serif; font-size: 30px; color: var(--navy); }

  /* Services */
  .services { top: 1368px; height: 342px; background: var(--band); }
  .services .section-title { position: absolute; top: 54px; width: 1200px; text-align: center; }
  .service { position: absolute; top: 135px; display: flex; gap: 22px; }
  .service-photo { width: 209px; height: 142px; }
  .service-body { width: 270px; }
  .service-title { font-family: "Roboto Condensed", sans-serif; font-weight: 400; font-size: 26px; color: var(--blue); line-height: 1.1; margin-top: -2px; }
  .service-text { font-size: 15.5px; line-height: 25px; margin-top: 10px; }
  .read-more { font-family: "Open Sans", sans-serif; font-weight: 700; font-size: 15px; color: var(--navy); margin-top: 6px; display: flex; align-items: center; gap: 4px; }

  /* Newsletter */
  .newsletter { top: 1710px; height: 126px; background: var(--navy); }
  .newsletter-title { position: absolute; left: 118px; top: 34px; font-family: "Cinzel", serif; font-size: 39px; color: var(--white); white-space: nowrap; }
  .newsletter-field { position: absolute; left: 433px; top: 32px; width: 365px; height: 51px; border: 1.5px solid var(--white); color: var(--white); font-size: 16px; padding: 14px 12px; }
  .newsletter-btn { position: absolute; left: 798px; top: 32px; width: 167px; height: 51px; background: var(--white); color: var(--navy); font-family: "Cinzel", serif; font-size: 20px; display: flex; align-items: center; justify-content: center; letter-spacing: 1px; }

  /* Footer */
  .site-footer { top: 1836px; height: 351px; background: var(--footer); color: var(--white); }
  .footer-brand { position: absolute; left: 80px; top: 40px; width: 210px; }
  .footer-square { width: 60px; height: 60px; background: var(--white); margin: 0 0 0 75px; }
  .footer-name { font-family: "Cinzel", serif; font-size: 22px; margin-top: 40px; white-space: nowrap; text-align: center; }
  .footer-tag { font-family: "Cinzel", serif; font-size: 8px; letter-spacing: 3px; text-align: center; border-top: 1px solid #aaa; margin-top: 6px; padding-top: 4px; width: 206px; white-space: nowrap; }
  .footer-about { font-size: 15px; line-height: 25px; margin-top: 14px; }
  .footer-col { position: absolute; top: 34px; }
  .footer-heading { font-family: "Cinzel", serif; font-size: 23px; margin-bottom: 12px; }
  .link-list { list-style: none; font-size: 17.5px; line-height: 33.5px; }
  .link-list li { display: flex; align-items: center; gap: 8px; }
  .news-item { font-size: 15.5px; line-height: 22px; margin-bottom: 18px; }
  .news-date { font-size: 14px; color: #aaaaaa; display: flex; align-items: center; gap: 5px; }
  .contact-row { display: flex; gap: 12px; font-size: 15.5px; line-height: 22px; margin-bottom: 14px; }
  .contact-row.phone { font-weight: 700; }
  .social { display: flex; gap: 20px; margin-top: 4px; }
  .social span { width: 52px; height: 52px; border-radius: 50%; border: 1.5px solid var(--white); }
  .social span:first-child { background: var(--white); }
  .footer-rule { position: absolute; left: 77px; top: 300px; width: 1046px; border-top: 1px solid var(--footer-line); }
  .copyright { position: absolute; top: 315px; width: 1200px; text-align: center; font-size: 15.5px; }
</style>
</head>
<body>

<header class="site-header">
  <div class="brand">
    <div class="brand-square"></div>
    <div class="brand-text">
      <span class="brand-name">Brook Vantage</span>
      <span class="brand-tag">Claims Recovery Services</span>
    </div>
  </div>
  <nav class="main-nav">
    <span class="active">HOME</span><span>ABOUT</span><span>SERVICES</span><span>CLIENTS</span><span>BLOG</span><span>CONTACT</span>
  </nav>
</header>

<section class="hero" role="img" aria-label="Desk with an open book, a pen and a calculator in soft light">
  <h1 class="hero-headline">Managing your money,<br>recovering your<br>relationships</h1>
  <div class="btn-outline">CONTACT US</div>
</section>

<section class="sectors">
  <div class="sector" style="left:65px">
    <div class="sector-icon">
      <svg width="56" height="52" viewBox="0 0 56 52" fill="#234f75"><polygon points="28,2 54,14 2,14"/><rect x="4" y="16" width="48" height="4"/><rect x="9" y="22" width="6" height="20"/><rect x="19" y="22" width="6" height="20"/><rect x="31" y="22" width="6" height="20"/><rect x="41" y="22" width="6" height="20"/><rect x="4" y="44" width="48" height="6"/></svg>
    </div>
    <div class="sector-label">GOVERNMENT<br>ENTITIES</div>
  </div>
  <div class="sector" style="left:335px">
    <div class="sector-icon">
      <svg width="54" height="48" viewBox="0 0 54 48"><path d="M27 46 C10 32 2 24 2 14 A12 12 0 0 1 27 8 A12 12 0 0 1 52 14 C52 24 44 32 27 46Z" fill="#234f75"/><polyline points="8,24 20,24 24,16 29,32 33,22 46,22" fill="none" stroke="#fff" stroke-width="3"/></svg>
    </div>
    <div class="sector-label">MEDICAL &amp; HEALTH<br>CARE</div>
  </div>
  <div class="sector" style="left:606px">
    <div class="sector-icon">
      <svg width="34" height="58" viewBox="0 0 34 58"><path d="M29 16 C27 10 22 8 17 8 C10 8 5 11 5 17 C5 30 30 26 30 40 C30 47 24 50 17 50 C10 50 5 47 3 41" fill="none" stroke="#234f75" stroke-width="6"/><rect x="14" y="1" width="6" height="56" fill="#234f75"/></svg>
    </div>
    <div class="sector-label">BANKS &amp; FINANCE<br>COMPANIES</div>
  </div>
  <div class="sector" style="left:876px">
    <div class="sector-icon">
      <svg width="62" height="40" viewBox="0 0 62 40" fill="none" stroke="#234f75" stroke-width="3.5" stroke-linejoin="round"><path d="M2 8 L12 4 L20 22 L12 26Z" fill="#234f75"/><path d="M60 8 L50 4 L42 22 L50 26Z" fill="#234f75"/><path d="M16 22 L28 34 C30 36 33 34 31 31 M24 28 L32 36 C34 38 37 35 35 33 M30 26 L38 34 C40 35 42 32 40 30 L32 22"/><path d="M46 20 L34 10 L26 14 C23 16 22 12 25 10 L32 6 L46 8"/></svg>
    </div>
    <div class="sector-label">SME'S &amp; COMMERCIAL<br>BUSINESS</div>
  </div>
</section>

<section class="welcome">
  <h2 class="section-title">WELCOME TO <strong>BROOK VANTAGE</strong></h2>
  <p class="welcome-copy">We are a Claims Recovery and Debt Management Services company based in Dubai, United Arab Emirates. The Brook Vantage team handles a comprehensive range of debt recoveries, such as invoices; insurance payments; supplier and rent payments; and personal and business loans, for individuals and businesses across an array of industries.</p>
  <div class="btn-outline">READ MORE</div>
  <div class="welcome-mark" role="img" aria-label="Brook Vantage name on a soft grey panel">BROOK VANTAGE</div>
</section>

<section class="services">
  <h2 class="section-title">SERVICES <strong>WE PROVIDE</strong></h2>
  <article class="service" style="left:80px">
    <div class="service-photo" role="img" aria-label="Business team meeting in a bright office" style="background:linear-gradient(135deg,#cfe0ee,#9fb6c9 55%,#6f7f8f)"></div>
    <div class="service-body">
      <h3 class="service-title">Recovery Solutions</h3>
      <p class="service-text">Our experience has taught us that when it comes to recovery, it always pays to find the most amicable...</p>
      <div class="read-more">READ MORE <svg width="14" height="12" viewBox="0 0 14 12" fill="none" stroke="#234f75" stroke-width="2"><polyline points="1,1 6,6 1,11"/><polyline points="7,1 12,6 7,11"/></svg></div>
    </div>
  </article>
  <article class="service" style="left:628px">
    <div class="service-photo" role="img" aria-label="Stacks of coins beside a glowing light bulb" style="background:linear-gradient(90deg,#6d7480,#a9a394 45%,#d8ccad 70%,#5f656f)"></div>
    <div class="service-body">
      <h3 class="service-title">Debt Management</h3>
      <p class="service-text">At Brook Vantage, we pull together our wisdom and expertise to make debt work for you...</p>
      <div class="read-more">READ MORE <svg width="14" height="12" viewBox="0 0 14 12" fill="none" stroke="#234f75" stroke-width="2"><polyline points="1,1 6,6 1,11"/><polyline points="7,1 12,6 7,11"/></svg></div>
    </div>
  </article>
</section>

<section class="newsletter">
  <h2 class="newsletter-title">NEWSLETTER</h2>
  <div class="newsletter-field">Enter Email Id</div>
  <div class="newsletter-btn">SUBSCRIBE</div>
</section>

<footer class="site-footer">
  <div class="footer-brand">
    <div class="footer-square"></div>
    <div class="footer-name">BROOK VANTAGE</div>
    <div class="footer-tag">CLAIMS RECOVERY SERVICES</div>
    <p class="footer-about">We are a Claims Recovery and Debt Management Services company based in Dubai.</p>
  </div>

  <div class="footer-col" style="left:351px">
    <h4 class="footer-heading">USEFUL LINKS</h4>
    <ul class="link-list">
      <li><svg width="8" height="14" viewBox="0 0 8 14" fill="none" stroke="#fff" stroke-width="1.6"><polyline points="1,1 7,7 1,13"/></svg>Home</li>
      <li><svg width="8" height="14" viewBox="0 0 8 14" fill="none" stroke="#fff" stroke-width="1.6"><polyline points="1,1 7,7 1,13"/></svg>About</li>
      <li><svg width="8" height="14" viewBox="0 0 8 14" fill="none" stroke="#fff" stroke-width="1.6"><polyline points="1,1 7,7 1,13"/></svg>Services</li>
      <li><svg width="8" height="14" viewBox="0 0 8 14" fill="none" stroke="#fff" stroke-width="1.6"><polyline points="1,1 7,7 1,13"/></svg>Clients</li>
      <li><svg width="8" height="14" viewBox="0 0 8 14" fill="none" stroke="#fff" stroke-width="1.6"><polyline points="1,1 7,7 1,13"/></svg>Blog</li>
      <li><svg width="8" height="14" viewBox="0 0 8 14" fill="none" stroke="#fff" stroke-width="1.6"><polyline points="1,1 7,7 1,13"/></svg>Contact</li>
    </ul>
  </div>

  <div class="footer-col" style="left:589px">
    <h4 class="footer-heading">LATEST NEWS</h4>
    <div class="news-item">Lorem Ipsum is simply dummy.<div class="news-date"><svg width="12" height="12" viewBox="0 0 12 12" fill="#aaa"><rect x="0" y="2" width="12" height="10" rx="1"/><rect x="2" y="0" width="2" height="3"/><rect x="8" y="0" width="2" height="3"/></svg>20 May 2016</div></div>
    <div class="news-item">Lorem Ipsum is simply dummy.<div class="news-date"><svg width="12" height="12" viewBox="0 0 12 12" fill="#aaa"><rect x="0" y="2" width="12" height="10" rx="1"/><rect x="2" y="0" width="2" height="3"/><rect x="8" y="0" width="2" height="3"/></svg>20 May 2016</div></div>
    <div class="news-item">Lorem Ipsum is simply dummy.<div class="news-date"><svg width="12" height="12" viewBox="0 0 12 12" fill="#aaa"><rect x="0" y="2" width="12" height="10" rx="1"/><rect x="2" y="0" width="2" height="3"/><rect x="8" y="0" width="2" height="3"/></svg>20 May 2016</div></div>
  </div>

  <div class="footer-col" style="left:892px">
    <h4 class="footer-heading">GET IN TOUCH</h4>
    <div class="contact-row"><svg width="14" height="20" viewBox="0 0 14 20"><path d="M7 0 A7 7 0 0 1 14 7 C14 12 7 20 7 20 C7 20 0 12 0 7 A7 7 0 0 1 7 0Z" fill="#fff"/><circle cx="7" cy="7" r="2.6" fill="#333"/></svg><span>Lorem Ipsum is dummy<br>text of the printing.</span></div>
    <div class="contact-row phone"><svg width="18" height="18" viewBox="0 0 24 24" fill="#fff"><path d="M6.6 10.8a15.1 15.1 0 0 0 6.6 6.6l2.2-2.2c.3-.3.7-.4 1-.2 1.1.4 2.3.6 3.6.6.6 0 1 .4 1 1V20c0 .6-.4 1-1 1A17 17 0 0 1 3 4c0-.6.4-1 1-1h3.5c.6 0 1 .4 1 1 0 1.3.2 2.5.6 3.6.1.3 0 .7-.2 1z"/></svg><span>123 456 7890</span></div>
    <div class="contact-row"><svg width="18" height="14" viewBox="0 0 18 14" fill="none" stroke="#fff" stroke-width="1.6"><rect x="1" y="1" width="16" height="12" rx="1"/><polyline points="1,1 9,8 17,1"/></svg><span>info@brookvantage.com</span></div>
    <div class="social"><span></span><span></span><span></span></div>
  </div>

  <div class="footer-rule"></div>
  <p class="copyright">© <strong>BROOK VANTAGE</strong> - 2016. All Rights Reserved.</p>
</footer>

</body>
</html>
```